Software As A Service Tool Seeks Website Design

Please design the Homepage for the original competition. If you win the competition, you will design the other inner pages.

The website should be professional, futuristic, and upmarket.

Vondel is an online SAAS (Software as a Service) tool that offers the most effective means to give rapid and deep insights into groups of electronic documents.

It is private and secure and uses a range of software including AIs that analyse all the documents and aids users to quickly identify, query and draw conclusions from the data provided.

It will initially be developed for Data Rooms for the finance community (M&A, Finance and Investments).

Target Market(s)

Lawyers, Account managers, Due diligence persons. M&A Businesses

Industry/Entity Type

Data due diligence

Number of Pages Required

5+ page

Colors

Designer to choose colors to be used in the design.

Requirements
Must have
• Attention to detail, consistency of colours, shapes, and layout. Upmarket design.
Nice to have
• Creativity on design. Overall consistency of design and text. Colours that work together - here are the main Vondel colours Vondel: Vondel Blue: #177494 Lighter Blue: #d8e2e5 Mid Grey: #7a8083 Action Green: #4aab32 Normal Font Grey: #212121
Should not have
• Overuse of bright colours, inconsistent text size or fonts. unlicensed images.

```html
<!DOCTYPE html>
<html lang="en">
<head>
<meta charset="utf-8">
<title>Vondel – Fast and Secure Data Insights</title>
<link href="https://fonts.googleapis.com/css2?family=Inter:wght@300;400;500;600;700&display=swap" rel="stylesheet">
<style>
:root{
  --grey:#75797b;
  --blue:#327996;
  --blue-mid:#76a9be;
  --blue-soft:#cbe1ea;
  --blue-pale:#e3eef3;
  --blue-mist:#e9f0f4;
  --off:#f4f5f6;
  --text:#4a4f52;
  --dark:#212121;
  --green:#4aab32;
  --line:#b9d4df;
}
*{margin:0;padding:0;box-sizing:border-box}
html,body{width:1200px;height:3450px;overflow:hidden}
body{font-family:"Inter",Arial,sans-serif;background:#fff;color:var(--text);position:relative}
.abs{position:absolute}
.brand{font-weight:600;color:var(--blue);letter-spacing:.5px}
.btn{display:inline-flex;align-items:center;gap:10px;font-size:11px;font-weight:500;padding:0 14px;height:30px;border-radius:3px;text-decoration:none}
.btn svg{width:12px;height:8px}
.btn-solid{background:var(--blue);color:#fff}
.btn-line{border:1px solid var(--blue-mid);color:var(--blue);background:#fff}
.btn-ghost{border:1px solid rgba(255,255,255,.8);color:#fff}
.h2{font-size:31px;font-weight:300;color:var(--blue);line-height:1.1}
.h2 b{font-weight:600}
.copy p{font-size:11px;line-height:1.6;margin-bottom:12px;color:var(--text)}
.copy p b{font-weight:600;color:var(--dark)}
.photo{border-radius:50%;overflow:hidden}
.ring{border:1.5px solid var(--line);border-radius:50%}
.mini{background:#fff;border-radius:3px;box-shadow:0 4px 14px rgba(0,0,0,.18);padding:6px}
.mini i{display:block;height:3px;background:#d6dfe3;margin:4px 0;border-radius:2px}
.mini i.b{background:var(--blue-mid);width:40%}

/* nav */
.nav{top:0;left:0;width:1200px;height:64px}
.nav .brand{left:160px;top:16px;font-size:26px}
.nav-util{right:160px;top:12px;font-size:8.5px;color:var(--grey);display:flex;gap:14px}
.nav-main{right:160px;top:34px;font-size:10px;color:var(--blue);display:flex;gap:58px}

/* hero */
.hero{top:64px;left:12px;width:1176px;height:370px;border-radius:8px;overflow:hidden;
  background:linear-gradient(100deg,#d6e7ee 0%,#e8f1f5 45%,#dbe9ef 100%)}
.hero h1{left:148px;top:108px;font-size:45px;font-weight:300;color:var(--blue);line-height:1.06;letter-spacing:-.3px}
.hero h1 b{font-weight:600}
.hero .btn{left:150px;top:247px}
.app{left:618px;top:52px;width:580px;height:302px;background:#fff;border-radius:8px;box-shadow:0 8px 24px rgba(50,121,150,.15)}
.app-side{left:0;top:0;width:34px;height:100%;border-right:1px solid var(--blue-pale)}
.app-side span{position:absolute;left:8px;width:18px;height:18px;border-radius:50%;border:1.5px solid var(--blue-mid)}
.app-cat{left:42px;top:12px;width:100px}
.app-cat .co{font-size:7.5px;font-weight:700;color:var(--blue)}
.app-cat .tag{font-size:5.5px;color:var(--green);margin:2px 0 0 48px}
.app-cat h4{font-size:14px;color:var(--blue);font-weight:600;margin:8px 0 4px}
.app-cat li{list-style:none;font-size:6.5px;color:var(--text);border:1px solid var(--blue-pale);border-radius:3px;padding:3px 5px;margin-bottom:4px;width:78px}
.app-ov{left:196px;top:12px;width:350px}
.app-ov .stats{font-size:6.5px;color:var(--grey);margin-bottom:8px}
.app-ov h4{font-size:12px;color:var(--blue);font-weight:600;margin-bottom:3px}
.app-ov h5{font-size:7px;color:var(--blue);font-weight:600;margin:5px 0 2px 120px}
.app-ov p{font-size:5.5px;line-height:1.45;color:var(--grey);margin-left:120px}
.app-ov p.first{margin-left:0}
.app-logo{left:510px;top:14px;font-size:17px}
.ai-badge{left:1010px;top:34px;width:62px;height:62px;border-radius:8px;background:var(--blue);color:#fff;font-size:8px;font-weight:600;display:flex;align-items:flex-end;justify-content:center;padding-bottom:9px}
.ai-badge::before{content:"";position:absolute;top:11px;left:21px;width:20px;height:20px;border:1.5px solid #fff;border-radius:50%}
.person{left:780px;top:118px;width:150px;height:252px;border-radius:70px 70px 0 0;background:linear-gradient(180deg,#b7c6cd,#8ea3ad 60%,#c9d6dc)}
.team{left:630px;top:318px;width:160px;height:36px;background:#fff;border-radius:18px;box-shadow:0 3px 10px rgba(0,0,0,.12);display:flex;align-items:center;gap:8px;padding:0 10px;font-size:7.5px;color:var(--dark);line-height:1.3}
.team .dots{display:flex}
.team .dots span{width:18px;height:18px;border-radius:50%;background:var(--blue-soft);border:2px solid #fff;margin-right:-6px}

/* feature rows */
.feature{left:0;width:1200px}
.feature .icon{width:26px;height:26px;margin-bottom:10px;display:block}
.feature .text{position:absolute;width:420px}
.connector{left:0;width:1200px;height:60px}

/* how it works */
.how{top:1816px;left:12px;width:1176px;height:450px;border-radius:6px;
  background:linear-gradient(180deg,#3d88a7 0%,#4f93af 45%,#3a84a3 100%);color:#fff;text-align:center}
.how h2{position:absolute;top:52px;width:100%;font-size:27px;font-weight:500}
.how .sub{position:absolute;top:100px;width:100%;font-size:10.5px;line-height:1.5;opacity:.85}
.step{position:absolute;width:276px;height:84px;border-radius:5px;background:rgba(255,255,255,.16);border:1px solid rgba(255,255,255,.35);
  display:flex;align-items:center;justify-content:center;gap:14px;font-size:10px;text-align:left;line-height:1.45}
.step .n{position:absolute;left:-6px;top:-6px;width:14px;height:14px;border-radius:50%;background:#fff;color:var(--blue);font-size:7.5px;font-weight:600;display:flex;align-items:center;justify-content:center}
.step svg{width:30px;height:30px}
.how .foot{position:absolute;top:370px;left:0;width:100%;display:flex;justify-content:center;align-items:center;gap:16px;font-size:8.5px}
.how .foot .rule{width:56px;height:1px;background:rgba(255,255,255,.6)}
.how .foot .btn{background:#fff;color:var(--blue);height:26px;font-size:8.5px}

/* trial */
.trial{top:2276px;left:12px;width:1176px;height:350px;border-radius:6px;background:linear-gradient(180deg,#dbe9ef,#eef4f7 50%,#dde9ee)}
.trial h2{position:absolute;top:48px;width:100%;text-align:center;font-size:27px;font-weight:500;color:var(--blue)}
.perks{position:absolute;top:100px;left:350px;width:500px;display:flex;justify-content:space-between;font-size:9.5px;color:var(--grey)}
.perks span{display:flex;align-items:center;gap:6px}
.perks b{font-weight:600;color:var(--dark)}
.perks svg{width:11px;height:11px}
.trial .actions{position:absolute;top:134px;left:0;width:100%;display:flex;justify-content:center;gap:10px}
.trial .actions .btn{height:26px;font-size:8.5px}

.tablet{left:397px;top:2472px;width:406px;height:250px;background:#2a2c2e;border-radius:14px;padding:10px}
.screen{position:relative;width:100%;height:100%;background:#fff;border-radius:4px;overflow:hidden}
.t-rail{position:absolute;left:0;top:0;width:22px;height:100%;background:var(--blue)}
.t-rail span{position:absolute;left:5px;width:12px;height:12px;border-radius:50%;border:1.3px solid #fff}
.t-welcome{position:absolute;left:22px;top:0;width:82px;height:100%;background:#eef2f4;padding:44px 0 0 8px}
.t-welcome h4{font-size:8px;color:var(--blue);font-weight:600}
.t-welcome p{font-size:4.5px;color:var(--grey)}
.t-logo{position:absolute;right:10px;top:8px;font-size:13px}
.t-main{position:absolute;left:114px;top:42px;right:8px}
.t-main h4{font-size:8px;color:var(--blue);font-weight:600}
.t-new{position:absolute;right:2px;top:0;background:var(--green);color:#fff;font-size:4px;padding:2px 6px;border-radius:2px}
.rooms{display:grid;grid-template-columns:1fr 1fr;gap:8px 12px;margin-top:12px}
.room{background:#eef2f4;border-radius:3px;padding:6px;height:76px;position:relative}
.room h5{font-size:5px;color:var(--blue);font-weight:700}
.room .tag{position:absolute;right:5px;top:3px;font-size:3.5px;color:#d5695b}
.room .st{font-size:4px;color:var(--grey);margin:3px 0}
.room .f{background:#fff;font-size:4px;padding:2px 4px;margin-bottom:2px;border-radius:1px;color:var(--text)}
.room .row{display:flex;gap:4px;margin-top:3px}
.room .row span{font-size:3.5px;padding:2px 5px;border-radius:1px;background:#fff}
.room .row span.go{background:var(--green);color:#fff}

/* news */
.news h2{position:absolute;top:2784px;width:1200px;text-align:center;font-size:27px;font-weight:500;color:var(--blue)}
.card{position:absolute;top:2846px;width:270px;height:192px;border:1px solid #e4ebee;border-radius:6px;background:#fff;padding:16px 18px}
.card h3{font-size:11px;font-weight:400;color:var(--dark);line-height:1.3;height:32px}
.card .pic{margin-top:6px;height:104px;border-radius:3px}
.card a{display:inline-block;margin-top:12px;font-size:8px;color:var(--blue);text-decoration:none}

/* footer */
.footer{top:3062px;left:12px;width:1176px;height:376px;border-radius:6px;color:#fff;
  background:linear-gradient(180deg,#3a84a3 0%,#3f89a8 55%,#8ebbcc 100%)}
.fcol{position:absolute;top:58px;font-size:9px;line-height:1.85}
.fcol h4{font-size:15px;font-weight:500;margin-bottom:10px}
.fcol p{opacity:.9}
.fcol .btn{margin-top:14px;height:26px;font-size:8.5px}
.partner{font-size:20px;font-weight:700;margin-top:14px;letter-spacing:.5px}
.fbar{position:absolute;bottom:16px;left:148px;right:148px;display:flex;justify-content:space-between;font-size:7.5px;color:var(--blue)}
</style>
</head>
<body>

<!-- navigation -->
<header class="abs nav">
  <div class="abs brand">vondel</div>
  <div class="abs nav-util"><span>Login</span><span>|</span><span>About Us</span><span>|</span><span>Book an Appointment</span><span>|</span><span>Contact Us</span></div>
  <nav class="abs nav-main"><span>How it Works</span><span>Privacy &amp; Security</span><span>News</span></nav>
</header>

<!-- hero -->
<section class="abs hero">
  <h1 class="abs"><b>Fast</b> and <b>Secure</b><br>Data Insights and<br>Data Analysis</h1>
  <a class="abs btn btn-solid">Book a Trial <svg viewBox="0 0 12 8"><path d="M0 4h11M8 1l3 3-3 3" stroke="#fff" fill="none"/></svg></a>

  <div class="abs app">
    <div class="abs app-side">
      <span style="top:10px;background:var(--blue);border-color:var(--blue)"></span>
      <span style="top:40px;border:none"></span>
      <span style="top:66px;background:var(--green);border-color:var(--green)"></span>
      <span style="top:94px;border-radius:3px"></span>
      <span style="top:122px"></span>
    </div>
    <div class="abs app-cat">
      <div class="co">Harwick Antiques Ltd</div>
      <div class="tag">Change Room</div>
      <h4>Category</h4>
      <ul>
        <li>Summary &amp; Background</li><li>Owners &amp; Managers</li><li>Commercial</li><li>Finance &amp; Accounts</li>
        <li>Tax</li><li>Cultural</li><li>Legal</li><li>Technology</li><li>People</li>
      </ul>
    </div>
    <div class="abs app-ov">
      <div class="stats">▢ 260 &nbsp; ◌ 450 &nbsp; ◯ 92 &nbsp; ◯ 3</div>
      <h4>Overview</h4>
      <p class="first">Harwick Antiques is a furniture and decor supplier with a long trading history and a loyal customer base across several regions. The group sells through showrooms and online channels.</p>
      <h5>Ownership &amp; Management</h5>
      <p>Family held, with a small board and clear succession plans in place for the coming years.</p>
      <h5>Financial Performance &amp; Market Position</h5>
      <p>Revenue has grown steadily, margins remain healthy and the order book is stable.</p>
      <h5>Legal &amp; Compliance</h5>
      <p>No open disputes are recorded and core contracts have been reviewed.</p>
      <h5>Technology &amp; Data Protection</h5>
      <p>Systems are current, backed up daily and aligned with data rules.</p>
      <h5>Employee Relations</h5>
      <p>Staff turnover is low and training records are complete.</p>
    </div>
    <div class="abs app-logo brand">vondel</div>
  </div>
  <div class="abs ai-badge">AI-Based</div>
  <div class="abs person" role="img" aria-label="Photo of a business professional reading a tablet"></div>
  <div class="abs team"><div class="dots"><span></span><span></span><span></span></div><div style="margin-left:6px">Add your team<br>of collaborators</div></div>
</section>

<!-- data rooms -->
<section class="abs feature" style="top:480px;height:430px">
  <div class="abs ring" style="left:160px;top:50px;width:300px;height:300px"></div>
  <div class="abs photo" role="img" aria-label="Glowing blue cloud over a circuit board" style="left:172px;top:62px;width:276px;height:276px;background:radial-gradient(circle at 50% 40%,#5fc4e6,#1b5f85 55%,#0b2a44)"></div>
  <div class="abs mini" style="left:146px;top:246px;width:96px;height:66px"><i class="b"></i><i></i><i></i><i style="width:70%"></i><i></i><i style="width:60%"></i></div>
  <div class="text" style="left:620px;top:20px">
    <svg class="icon" viewBox="0 0 26 26" fill="none" stroke="var(--grey)" stroke-width="1.3"><path d="M4 24V12M10 24V6M16 24V10M22 24V4M2 24h22"/></svg>
    <h2 class="h2"><b>Data Rooms:</b> Oceans of<br>Data expensive to<br>trawl Through</h2>
    <div class="copy" style="margin-top:20px">
      <p style="color:var(--dark)">Data rooms are an essential part and yet for almost everyone involved it can be the most frustrating part of the process. The larger it is, the harder to find the information you want.</p>
      <p>It's time to stop hunting around file structures, looking for info that isn't there, sourcing data from different places, getting stuck with versions and wasting too much time failing to get the answers you need to help you maintain momentum.</p>
      <p>So, we came up with Vondel. Private, secure and fast data room analysis can be yours. Book a call to demo the app!</p>
    </div>
  </div>
</section>
<svg class="abs connector" style="top:912px" viewBox="0 0 1200 60" fill="none" stroke="var(--line)" stroke-width="1.5"><path d="M505 6c0 22 20 26 60 26h120c40 0 60 6 60 28"/></svg>

<!-- save time -->
<section class="abs feature" style="top:978px;height:430px">
  <div class="text" style="left:160px;top:0">
    <svg class="icon" viewBox="0 0 26 26" fill="none" stroke="var(--grey)" stroke-width="1.3"><circle cx="12" cy="13" r="10"/><path d="M12 7v6l4 3"/></svg>
    <h2 class="h2"><b>Save Time:</b> Spot Issues<br>and Collaborate</h2>
    <div class="copy" style="margin-top:20px">
      <p style="color:var(--dark)">With Vondel, you can <b>save days of high-ticket time</b>. Hunting around for the right file through a network of folders is frustrating, or compiling information from multiple sources can take hours. With Vondel you get an immediate detailed insight report which can be refreshed everytime you add new documents; and you have a conversational AI that gives detailed answers and references to you specific questions.</p>
      <p>The Insight Report also quickly spots any <b>critical information that is missing</b> from the Data Room and gives you the information you need for information requests.</p>
      <p>And the room, though fully secure, will allow you to share all this added value with you advisors, all for one fee. Meaning that you can work collaboratively with Corporate Finance, Accountants, Lawyers and Advisory firms, making the process efficient.</p>
    </div>
  </div>
  <div class="abs ring" style="left:700px;top:50px;width:300px;height:300px"></div>
  <div class="abs photo" role="img" aria-label="People working amid blue holographic data streams" style="left:712px;top:62px;width:276px;height:276px;background:radial-gradient(circle at 55% 45%,#4aa9cf,#1a4e72 55%,#0a2237)"></div>
  <div class="abs mini" style="left:900px;top:58px;width:90px;height:58px"><i class="b"></i><i></i><i></i><i style="width:60%"></i><i></i></div>
</section>
<svg class="abs connector" style="top:1410px" viewBox="0 0 1200 60" fill="none" stroke="var(--line)" stroke-width="1.5"><path d="M728 4c0 22-20 26-60 26H560c-40 0-60 6-60 26"/></svg>

<!-- privacy -->
<section class="abs feature" style="top:1478px;height:320px">
  <div class="abs ring" style="left:160px;top:0;width:300px;height:300px"></div>
  <div class="abs photo" role="img" aria-label="Robot facing a holographic security shield" style="left:172px;top:12px;width:276px;height:276px;background:radial-gradient(circle at 60% 45%,#9fd0e4,#3e7fa0 50%,#12324b)"></div>
  <div class="abs mini" style="left:206px;top:226px;width:96px;height:68px"><i class="b"></i><i></i><i></i><i style="width:70%"></i><i></i><i style="width:50%"></i></div>
  <div class="text" style="left:624px;top:8px">
    <svg class="icon" viewBox="0 0 26 26" fill="none" stroke="var(--grey)" stroke-width="1.3"><ellipse cx="11" cy="6" rx="8" ry="3"/><path d="M3 6v12c0 2 4 3 8 3M19 6v5"/><rect x="15" y="15" width="9" height="8" rx="1"/><path d="M17 15v-2a2.5 2.5 0 015 0v2"/></svg>
    <h2 class="h2" style="font-weight:600">Privacy &amp; Security:</h2>
    <div class="copy" style="margin-top:20px">
      <p>Your Vondel room is secure, and encrypted at rest. We do not train our systems on your data or pass to any insecure third-party companies. Only those authorised by you can see your documents.</p>
      <p style="margin-bottom:6px">With Vondel:</p>
    </div>
    <ul style="list-style:none;font-size:10px;color:var(--dark);line-height:2">
      <li><svg width="11" height="11" viewBox="0 0 12 12" fill="none" stroke="var(--blue-mid)"><circle cx="6" cy="6" r="5.2"/><path d="M3.5 6l2 2 3-4"/></svg>&nbsp; Each room is private and only seen by authorised users</li>
      <li><svg width="11" height="11" viewBox="0 0 12 12" fill="none" stroke="var(--blue-mid)"><circle cx="6" cy="6" r="5.2"/><path d="M3.5 6l2 2 3-4"/></svg>&nbsp; You have full administration of access to each room</li>
      <li><svg width="11" height="11" viewBox="0 0 12 12" fill="none" stroke="var(--blue-mid)"><circle cx="6" cy="6" r="5.2"/><path d="M3.5 6l2 2 3-4"/></svg>&nbsp; When deleted, a room is permanently erased</li>
    </ul>
    <a class="btn btn-line" style="margin-top:14px;height:26px;font-size:8.5px">Explore More <svg viewBox="0 0 12 8"><path d="M0 4h11M8 1l3 3-3 3" stroke="currentColor" fill="none"/></svg></a>
  </div>
</section>

<!-- how it works -->
<section class="abs how">
  <h2>How Vondel Works</h2>
  <p class="sub">Your Vondel room is secure, and encrypted at rest. We do not<br>train ou rsystems on your data.</p>
  <div class="step" style="left:298px;top:146px"><span class="n">1</span>
    <svg viewBox="0 0 30 30" fill="none" stroke="#fff" stroke-width="1.3"><path d="M8 4h10l6 6v16H8z"/><path d="M16 22v-10M12 16l4-4 4 4"/></svg>Upload Your Data Room</div>
  <div class="step" style="left:602px;top:146px"><span class="n">2</span>
    <svg viewBox="0 0 30 30" fill="none" stroke="#fff" stroke-width="1.3"><circle cx="13" cy="13" r="9"/><path d="M20 20l7 7M9 13l3 3 5-6"/></svg>Vondel analyses and<br>categorises your files</div>
  <div class="step" style="left:298px;top:254px"><span class="n">4</span>
    <svg viewBox="0 0 30 30" fill="none" stroke="#fff" stroke-width="1.3"><circle cx="13" cy="13" r="9"/><path d="M20 20l7 7M9 13l3 3 5-6"/></svg>Vondel answers any question<br>and references the source</div>
  <div class="step" style="left:602px;top:254px"><span class="n">3</span>
    <svg viewBox="0 0 30 30" fill="none" stroke="#fff" stroke-width="1.3"><circle cx="8" cy="7" r="4"/><path d="M15 5h12M15 9h9M4 27V19h4v8M11 27V15h4v12M18 27V18h4v9M25 27V13h3v14M2 27h27"/></svg>After Vondel's analysis,<br>you get 60 key insights</div>
  <div class="foot"><span>All within Minutes of Setup *</span><span class="rule"></span>
    <a class="btn">Find Out More <svg viewBox="0 0 12 8"><path d="M0 4h11M8 1l3 3-3 3" stroke="currentColor" fill="none"/></svg></a></div>
</section>

<!-- free trial -->
<section class="abs trial">
  <h2>Claim a Free Trial</h2>
  <div class="perks">
    <span><svg viewBox="0 0 12 12" fill="none" stroke="var(--blue-mid)"><circle cx="6" cy="6" r="5.2"/><path d="M3.5 6l2 2 3-4"/></svg><b>Free room</b> for 14 days</span>
    <span><svg viewBox="0 0 12 12" fill="none" stroke="var(--blue-mid)"><circle cx="6" cy="6" r="5.2"/><path d="M3.5 6l2 2 3-4"/></svg>Free room data size up to <b>1gb</b></span>
    <span><svg viewBox="0 0 12 12" fill="none" stroke="var(--blue-mid)"><circle cx="6" cy="6" r="5.2"/><path d="M3.5 6l2 2 3-4"/></svg><b>Unlimited</b> users</span>
  </div>
  <div class="actions">
    <a class="btn btn-solid">Book Meeting <svg viewBox="0 0 12 8"><path d="M0 4h11M8 1l3 3-3 3" stroke="#fff" fill="none"/></svg></a>
    <a class="btn btn-line">Contact Us <svg viewBox="0 0 12 8"><path d="M0 4h11M8 1l3 3-3 3" stroke="currentColor" fill="none"/></svg></a>
  </div>
</section>

<div class="abs tablet">
  <div class="screen">
    <div class="t-rail">
      <span style="top:8px"></span><span style="top:28px;background:var(--green);border-color:var(--green)"></span>
      <span style="top:56px"></span><span style="top:76px;border-radius:2px"></span><span style="top:100px"></span>
    </div>
    <div class="t-welcome"><h4>Welcome</h4><p>Mara Holloway</p></div>
    <div class="t-logo brand">vondel</div>
    <div class="t-main">
      <h4>Choose a Room</h4><span class="t-new">Create a New Room</span>
      <div class="rooms">
        <div class="room"><span class="tag">Uploaded</span><h5>Harwick Antiques Ltd</h5><div class="st">▢ 260 ◌ 450 ◯ 92 ◯ 3</div>
          <div class="f">Ask a Question</div><div class="f">Browse Insights</div><div class="f">Search Files</div>
          <div class="row"><span class="go">Enter</span><span>+ Add Files</span></div></div>
        <div class="room"><span class="tag">Uploaded</span><h5>Project Meridian</h5><div class="st">▢ 180 ◌ 310 ◯ 64 ◯ 5</div>
          <div class="f">Ask a Question</div><div class="f">Browse Insights</div><div class="f">Search Files</div>
          <div class="row"><span class="go">Enter</span><span>+ Add Files</span></div></div>
        <div class="room"><span class="tag">Uploaded</span><h5>Northgate Commerce Ltd</h5><div class="st">▢ 140 ◌ 220 ◯ 48 ◯ 2</div>
          <div class="f">Ask a Question</div></div>
        <div class="room"><span class="tag">Uploaded</span><h5>Linden Pharmacies</h5><div class="st">▢ 95 ◌ 160 ◯ 30 ◯ 4</div>
          <div class="f">Ask a Question</div></div>
      </div>
    </div>
  </div>
</div>

<!-- news -->
<section class="news">
  <h2>Vondel News</h2>
  <article class="card" style="left:160px"><h3>Tackling the challenges of<br>hallucination in AI</h3>
    <div class="pic" role="img" aria-label="White humanoid robot in thought" style="background:linear-gradient(135deg,#d9dee1,#8e979c 60%,#e8ecee)"></div>
    <a>Full Story →</a></article>
  <article class="card" style="left:465px"><h3>How to use AI effectively:<br>The perfect brief</h3>
    <div class="pic" role="img" aria-label="Hand reaching toward a glowing blue keyboard" style="background:linear-gradient(135deg,#bfe3f1,#4f9fc4 55%,#1e5a7e)"></div>
    <a>Full Story →</a></article>
  <article class="card" style="left:770px"><h3>How can you stop AI from<br>leaking confidential info?</h3>
    <div class="pic" role="img" aria-label="Robot beside a digital padlock" style="background:linear-gradient(135deg,#9aa7ae,#3b5f78 55%,#0f2a40)"></div>
    <a>Full Story →</a></article>
</section>

<!-- footer -->
<footer class="abs footer">
  <div class="fcol" style="left:148px;width:200px">
    <h4>Free Trial</h4><p>Set up your first Vondel and have<br>14 days to trial our solution</p>
    <a class="btn btn-ghost">Book a Trial <svg viewBox="0 0 12 8"><path d="M0 4h11M8 1l3 3-3 3" stroke="#fff" fill="none"/></svg></a>
  </div>
  <div class="fcol" style="left:428px">
    <h4>Explore</h4><p>How it Works<br>Pricing<br>Privacy &amp; Security<br>News<br>Vondel Login</p>
  </div>
  <div class="fcol" style="left:616px;width:190px">
    <h4>About Us</h4><p>Created in partnership with an AI pioneer, curated to the M&amp;A space and incubated by Keystra</p>
    <div class="partner">keystra</div>
  </div>
  <div class="fcol" style="left:897px">
    <h4>Contact</h4><p>Vondel AI Limited<br>Second Floor<br>Harbour Point House<br>Ashford<br>AF3 2QL</p>
    <a class="btn" style="background:#fff;color:var(--blue)">Appointment <svg viewBox="0 0 12 8"><path d="M0 4h11M8 1l3 3-3 3" stroke="currentColor" fill="none"/></svg></a>
  </div>
  <div class="fbar"><span>© 2024 Vondel - All Rights Reserved</span><span>Sitemap &nbsp;|&nbsp; Terms of Use &nbsp;|&nbsp; Privacy Policy</span></div>
</footer>

</body>
</html>
```